Halvorsen Partners Business Card

Halvorsen Partners Civil Construction
Marcus Halvorsen
CEO
727-518-6094
Marcus@HalvorsenSiteworks.example
www.HalvorsenSiteworks.example
Site Development
Utility Construction
Excavation
40876 County Lane 19
Cedar Hollow, FL 34782

Target Market(s)

Construction and government

Industry/Entity Type

Business

Contact Information for Business Card

I want an unique design that make a statement

Number of Pages Required

1 page

Font styles to use

Colors

Designer to choose colors to be used in the design.

Requirements
Must have
• unique design, feel free to modify or change the color of my logo.
Nice to have
• extra design features like spot UV, foil accents, color edges, unique paper, or any thing that would make my card pop.
• I like the feel of the image that I attached

```html
<!DOCTYPE html>
<html lang="en">
<head>
<meta charset="utf-8">
<title>Halvorsen Partners Business Card</title>
<link rel="stylesheet" href="https://fonts.googleapis.com/css2?family=Lato:wght@400;700;900&family=Open+Sans:wght@400;600&display=swap">
<style>
  :root {
    --stage: #6e6e6e;
    --edge-blue: #1f49ab;
    --edge-blue-light: #3c6fd6;
    --brand-navy: #35358a;
    --name-blue: #2c55a9;
    --text-navy: #1e2a5a;
    --muted-grey: #8a8a8a;
    --label-grey: #9b9b9b;
    --paper: #ffffff;
    --sky-top: #5f6677;
    --sky-mid: #9aa3b4;
    --ground: #1b202b;
    --silver: #c7ccd6;
  }
  * { box-sizing: border-box; margin: 0; padding: 0; }
  html, body { width: 1200px; height: 1200px; overflow: hidden; }
  body {
    background: var(--stage);
    display: flex;
    flex-direction: column;
    align-items: center;
    justify-content: center;
    gap: 60px;
    font-family: "Lato", sans-serif;
  }
  .card {
    position: relative;
    width: 900px;
    height: 514px;
    padding: 24px;
    background: linear-gradient(135deg, var(--edge-blue) 0%, var(--edge-blue-light) 55%, var(--edge-blue) 100%);
    box-shadow: 0 8px 24px rgba(0,0,0,0.35);
  }
  .card-inner { position: relative; width: 100%; height: 100%; overflow: hidden; }

  /* Cover side */
  .cover-scene {
    position: absolute; inset: 0;
    background: linear-gradient(180deg, var(--sky-top) 0%, var(--sky-mid) 55%, #7d8596 72%, var(--ground) 78%, var(--ground) 100%);
  }
  .cover-brand {
    position: absolute; left: 0; right: 0; top: 150px;
    display: flex; align-items: center; justify-content: center; gap: 18px;
    color: var(--silver);
  }
  .brand-square { width: 54px; height: 54px; background: currentColor; flex: none; }
  .brand-rule { width: 2px; height: 62px; background: currentColor; flex: none; }
  .brand-name { font-size: 34px; font-weight: 400; letter-spacing: 1px; text-transform: uppercase; line-height: 1.1; }
  .brand-sub { font-size: 15px; letter-spacing: 7px; text-transform: uppercase; }
  .cover-services {
    position: absolute; left: 0; right: 0; bottom: 38px;
    text-align: center; color: #fff; font-size: 17px; font-weight: 700;
    letter-spacing: 0.5px; text-transform: uppercase;
  }

  /* Contact side */
  .contact-side .card-inner { background: var(--paper); }
  .contact-brand {
    position: absolute; left: 30px; top: 34px;
    display: flex; align-items: center; gap: 14px; color: var(--brand-navy);
  }
  .contact-brand .brand-square { width: 44px; height: 44px; }
  .contact-brand .brand-rule { width: 1px; height: 56px; background: var(--muted-grey); }
  .contact-brand .brand-name { font-size: 28px; }
  .contact-brand .brand-sub { font-size: 13px; letter-spacing: 6px; color: #555; }
  .person { position: absolute; left: 470px; top: 150px; }
  .person-name { font-size: 30px; font-weight: 900; color: var(--name-blue); letter-spacing: 1px; text-transform: uppercase; white-space: nowrap; }
  .person-title { font-size: 20px; color: var(--muted-grey); margin-top: 2px; }
  .address { position: absolute; left: 470px; top: 262px; font-family: "Open Sans", sans-serif; font-size: 16px; color: var(--text-navy); line-height: 1.4; }
  .address-rule { width: 32px; height: 2px; background: var(--text-navy); margin: 12px 0 14px; }
  .contact-line { display: flex; align-items: center; gap: 8px; font-size: 16px; line-height: 1.6; white-space: nowrap; }
  .contact-label {
    display: inline-block; width: 20px; height: 18px; background: var(--label-grey);
    color: #fff; font-size: 12px; font-weight: 600; text-align: center; line-height: 18px;
  }
  .edge-notch { position: absolute; right: -14px; top: 226px; }
</style>
</head>
<body>
  <section class="card cover-side">
    <div class="card-inner">
      <div class="cover-scene" role="img" aria-label="Muted blue-grey sky over a construction site with excavator silhouettes on the horizon"></div>
      <div class="cover-brand">
        <span class="brand-square"></span>
        <span class="brand-rule"></span>
        <div>
          <div class="brand-name">Halvorsen Partners</div>
          <div class="brand-sub">Civil Construction</div>
        </div>
      </div>
      <p class="cover-services">Site Development Utility Construction Excavation</p>
    </div>
  </section>

  <section class="card contact-side">
    <div class="card-inner">
      <div class="contact-brand">
        <span class="brand-square"></span>
        <span class="brand-rule"></span>
        <div>
          <div class="brand-name">Halvorsen Partners</div>
          <div class="brand-sub">Civil Construction</div>
        </div>
      </div>
      <div class="person">
        <h1 class="person-name">Marcus Halvorsen</h1>
        <p class="person-title">CEO</p>
      </div>
      <div class="address">
        <p>40876 County Lane 19</p>
        <p>Cedar Hollow, FL 34782</p>
        <div class="address-rule"></div>
        <p class="contact-line"><span class="contact-label">T</span>: 727-518-6094</p>
        <p class="contact-line"><span class="contact-label">M</span>: Marcus@HalvorsenSiteworks.example</p>
        <p class="contact-line"><span class="contact-label">W</span>: www.HalvorsenSiteworks.example</p>
      </div>
    </div>
    <svg class="edge-notch" width="28" height="40" viewBox="0 0 28 40" aria-hidden="true">
      <path d="M28 0 A20 20 0 0 0 28 40 Z" fill="var(--edge-blue)"/>
    </svg>
  </section>
</body>
</html>
```